Stationary Design Letterhead and Envelope

Artist should provide Letterhead and envelop stationary designs

Info for stationary:
Fernhallow Outdoor Advertising
4873 Quarry Rd. 915 N. PO BOX 528617
Austin, TX 78519

Dale Fernhallow
President
555-862-1907
dale@fernhallowsigns.example
fernhallowsigns.example

Target Market(s)

clients

Colors
0054AA
0677BA
7BADD7
CADEEF
E8F1F8

Requirements
Must have
• high quality unique eye catching and dynamic

```html
<!DOCTYPE html>
<html lang="en">
<head>
<meta charset="utf-8">
<title>Fernhallow Outdoor Advertising – Stationery</title>
<link rel="stylesheet" href="https://fonts.googleapis.com/css2?family=Questrial&display=swap">
<style>
  :root {
    --brand: #0b5496;
    --paper: #ffffff;
    --edge: #6f6f6f;
    --page-bg: #ffffff;
  }
  * { box-sizing: border-box; margin: 0; padding: 0; }
  html, body {
    width: 1000px; height: 1200px; overflow: hidden;
    background: var(--page-bg);
  }
  .canvas { position: relative; width: 1000px; height: 1200px; }
  .sheet {
    position: absolute; background: var(--paper);
    border: 1px solid var(--edge);
  }
  .letterhead { left: 39px; top: 89px; width: 766px; height: 990px; }
  .business-card { left: 421px; top: 381px; width: 317px; height: 181px; }
  .envelope { left: 106px; top: 620px; width: 856px; height: 373px; }

  .brand-mark { position: absolute; display: block; overflow: visible; }
  .brand-mark text { font-family: "Questrial", sans-serif; font-weight: 400; fill: var(--brand); }
  .brand-mark rect { fill: var(--brand); }

  .letterhead .brand-mark { left: 176px; top: 24px; width: 415px; height: 110px; }
  .business-card .brand-mark { left: 54px; top: 11px; width: 200px; height: 53px; }
  .envelope .brand-mark { left: 33px; top: 19px; width: 305px; height: 81px; }

  .address, .card-name, .card-title, .card-contact {
    position: absolute; font-family: "Questrial", sans-serif;
    color: var(--brand); white-space: nowrap;
  }
  .letterhead .address {
    left: 175px; width: 417px; top: 142px;
    text-align: center; font-size: 13px;
  }
  .envelope .address {
    left: 33px; width: 307px; top: 106px;
    text-align: center; font-size: 10px;
  }

  .card-name {
    left: 0; width: 100%; top: 82px; text-align: center;
    font-weight: 400; font-size: 15px; letter-spacing: 1px;
  }
  .card-title { left: 0; width: 100%; top: 106px; text-align: center; font-size: 9.5px; letter-spacing: 0.5px; }
  .card-contact { left: 0; width: 100%; text-align: center; font-size: 10px; }
  .card-contact.line-one { top: 136px; }
  .card-contact.line-two { top: 151px; }
  .sep { margin: 0 5px; }
  .letterhead .sep { margin: 0 9px; }
</style>
</head>
<body>
<div class="canvas">

  <section class="sheet letterhead">
    <svg class="brand-mark" viewBox="0 0 415 110" role="img" aria-label="Fernhallow Outdoor Advertising">
      <rect x="0" y="2" width="104" height="104"/>
      <text x="124" y="66" font-size="44" textLength="290" lengthAdjust="spacingAndGlyphs">FERNHALLOW</text>
      <text x="124" y="88" font-size="17" textLength="290" lengthAdjust="spacingAndGlyphs">OUTDOOR ADVERTISING</text>
      <text x="124" y="107" font-size="13" textLength="290" lengthAdjust="spacingAndGlyphs">FERNHALLOWSIGNS.EXAMPLE</text>
    </svg>
    <p class="address">4873 Quarry Road<span class="sep">•</span>915 N. PO Box 528617<span class="sep">•</span>Austin, TX&nbsp; 78519</p>
  </section>

  <section class="sheet business-card">
    <svg class="brand-mark" viewBox="0 0 415 110" role="img" aria-label="Fernhallow Outdoor Advertising">
      <rect x="0" y="2" width="104" height="104"/>
      <text x="124" y="66" font-size="44" textLength="290" lengthAdjust="spacingAndGlyphs">FERNHALLOW</text>
      <text x="124" y="88" font-size="17" textLength="290" lengthAdjust="spacingAndGlyphs">OUTDOOR ADVERTISING</text>
      <text x="124" y="107" font-size="13" textLength="290" lengthAdjust="spacingAndGlyphs">FERNHALLOWSIGNS.EXAMPLE</text>
    </svg>
    <h2 class="card-name">DALE FERNHALLOW</h2>
    <p class="card-title">PRESIDENT</p>
    <p class="card-contact line-one">4873 Quarry Road<span class="sep">•</span>915 N. PO Box 528617<span class="sep">•</span>Austin, TX&nbsp; 78519</p>
    <p class="card-contact line-two">PH: 555-862-1907<span class="sep">•</span>dale@fernhallowsigns.example</p>
  </section>

  <section class="sheet envelope">
    <svg class="brand-mark" viewBox="0 0 415 110" role="img" aria-label="Fernhallow Outdoor Advertising">
      <rect x="0" y="2" width="104" height="104"/>
      <text x="124" y="66" font-size="44" textLength="290" lengthAdjust="spacingAndGlyphs">FERNHALLOW</text>
      <text x="124" y="88" font-size="17" textLength="290" lengthAdjust="spacingAndGlyphs">OUTDOOR ADVERTISING</text>
      <text x="124" y="107" font-size="13" textLength="290" lengthAdjust="spacingAndGlyphs">FERNHALLOWSIGNS.EXAMPLE</text>
    </svg>
    <p class="address">4873 Quarry Road<span class="sep">•</span>915 N. PO Box 528617<span class="sep">•</span>Austin, TX&nbsp; 78519</p>
  </section>

</div>
</body>
</html>
```